Presentation Folder for A New Home Construction Company

We need a Presentation Folder for a new home construction company based in Perth, Australia. It's called Tarvo Homes and specialises in building quality homes that are affordable and people want to live in. The target market is first-home buyers.

We've rebranded the website (www.tarvohomes.com.au) and are looking to update our presentation folder to match it. We want red, white, grey and black as the colour palette, and some designs with transparent photos included but overall a minimalistic approach that aligns with our new website and vehicles.

I've attached an image of our updated car wrap, can you please follow this as a guide?

I've also attached our logo, style guide and past presentation folder for reference.

Please also include:

"Plan Well, Move In, Stay Put" - refer to the previous presentation folder.

Target Market(s)

First Home Buyers

Industry/Entity Type

New Home Construction

Font styles to use
Sans Serif
Other font styles liked:
• Monserrat

Colors
EB3D1F
EC4F4E
F09395
F8D3D4
FCEDEE

Requirements
Must have
• Monserrat or Open Sans Font and Include the colours from the attached brand guide, the contact details and address,
Nice to have
• some with a photo feature - but not the main component, very minimal.
Should not have
• Too many elements, (refer to previous folder attachment) animations or graphics.

```html
<!DOCTYPE html>
<html lang="en">
<head>
<meta charset="utf-8">
<title>Tarvo Homes Presentation Folder</title>
<link href="https://fonts.googleapis.com/css2?family=Montserrat:wght@400;500;700;800&display=swap" rel="stylesheet">
<style>
  :root {
    --bg-grey: #b1b2b5;
    --red-deep: #9e1b1a;
    --red-dark: #7a0d0b;
    --red-bright: #e23a2c;
    --red-head: #a51d1c;
    --white: #ffffff;
    --ink: #222222;
    --grey-text: #5b5b5e;
  }
  * { margin: 0; padding: 0; box-sizing: border-box; }
  html, body { width: 1200px; height: 898px; overflow: hidden; background: var(--bg-grey); }
  body { font-family: "Montserrat", Arial, sans-serif; color: var(--ink); }
  .canvas { position: relative; width: 1200px; height: 898px; }
  .dieline { position: absolute; left: 0; top: 0; }

  .inside-panel {
    position: absolute; left: 265px; top: 88px; width: 406px; height: 577px;
    background: linear-gradient(90deg, var(--white) 0%, var(--white) 78%, #e4e4e6 100%);
  }
  .brand-small {
    position: absolute; left: 24px; top: 62px;
    font-weight: 700; font-size: 22px; color: var(--grey-text); letter-spacing: 0.5px;
    display: flex; align-items: center; gap: 8px; white-space: nowrap;
  }
  .brand-small .mark { width: 12px; height: 12px; background: var(--red-bright); }
  .intro {
    position: absolute; left: 20px; top: 163px; width: 250px;
    font-size: 12.6px; line-height: 19.5px; color: var(--ink);
  }
  .slogan {
    position: absolute; left: 20px; top: 242px;
    font-weight: 700; font-size: 26px; line-height: 35px; white-space: nowrap;
  }
  .slogan span { display: block; color: var(--red-head); }
  .slogan .accent { color: var(--red-bright); }
  .director-photo {
    position: absolute; left: 226px; top: 224px; width: 180px; height: 236px;
    background: radial-gradient(ellipse at 60% 40%, #8a8f98 0%, #b6b9be 45%, rgba(255,255,255,0) 75%);
  }
  .signature {
    position: absolute; left: 70px; top: 405px; width: 132px; height: 36px;
    background: linear-gradient(90deg, rgba(226,58,44,0.15), rgba(226,58,44,0.3), rgba(226,58,44,0.15));
    border-radius: 18px;
  }
  .role {
    position: absolute; left: 95px; top: 442px;
    font-size: 8.6px; letter-spacing: 0.9px; color: var(--ink); white-space: nowrap;
  }
  .contacts {
    position: absolute; left: 33px; top: 513px; width: 339px;
    display: flex; align-items: center; justify-content: space-between;
    font-size: 8.8px; color: var(--ink); white-space: nowrap;
  }
  .contact { display: flex; align-items: center; gap: 3px; white-space: nowrap; }
  .contact svg { width: 10px; height: 10px; flex: none; }
  .rule { position: absolute; left: 33px; top: 532px; width: 339px; height: 1px; background: var(--red-bright); }
  .address {
    position: absolute; left: 33px; top: 537px; width: 339px;
    text-align: center; font-size: 9.4px; line-height: 11.5px; letter-spacing: 0.2px; color: var(--ink);
  }

  .cover-panel { position: absolute; left: 671px; top: 88px; width: 405px; height: 577px; background: var(--white); overflow: hidden; }
  .brand-large {
    position: absolute; left: 0; top: 100px; width: 405px; text-align: center;
    font-weight: 800; font-size: 40px; color: var(--grey-text); letter-spacing: 1px; white-space: nowrap;
  }
  .brand-large .mark { display: inline-block; width: 16px; height: 16px; background: var(--red-bright); margin-right: 10px; vertical-align: middle; }
  .cover-wave { position: absolute; left: 0; top: 0; }
</style>
</head>
<body>
<div class="canvas">
  <svg class="dieline" width="1200" height="898" viewBox="0 0 1200 898">
    <defs>
      <linearGradient id="flapLeft" x1="0" x2="1" y1="0" y2="0">
        <stop offset="0" stop-color="#a41d1b"/>
        <stop offset="0.7" stop-color="#9a1a18"/>
        <stop offset="1" stop-color="#7a0d0b"/>
      </linearGradient>
      <linearGradient id="pocket" x1="0" x2="0" y1="0" y2="1">
        <stop offset="0" stop-color="#7a0d0b"/>
        <stop offset="0.4" stop-color="#9a1a18"/>
        <stop offset="1" stop-color="#a41d1b"/>
      </linearGradient>
    </defs>
    <path class="left-flap" d="M125 120 Q125 88 157 88 H265 V665 L125 662 Z" fill="url(#flapLeft)"/>
    <path class="pocket-flap" d="M265 665 H671 V755 Q671 809 617 809 H390 Z" fill="url(#pocket)"/>
  </svg>

  <section class="inside-panel">
    <div class="brand-small"><span class="mark"></span>Tarvo Homes</div>
    <p class="intro">Offering first home buyers the same outstanding service &amp; innovation that has been Reid Calder’s hallmark for over 15 years.</p>
    <h2 class="slogan"><span>Plan Well…</span><span class="accent">Move In…</span><span>Stay Put.</span></h2>
    <div class="director-photo" role="img" aria-label="Photo of the managing director, fading into white"></div>
    <div class="signature" role="img" aria-label="Signature of Reid Calder"></div>
    <p class="role">MANAGING DIRECTOR</p>
    <div class="contacts">
      <span class="contact">
        <svg viewBox="0 0 12 12"><rect x="3" y="0.5" width="6" height="11" rx="1" fill="none" stroke="#a51d1c" stroke-width="1"/><line x1="5" y1="9.8" x2="7" y2="9.8" stroke="#a51d1c"/></svg>
        08 9400 1275
      </span>
      <span class="contact">
        <svg viewBox="0 0 12 12"><circle cx="6" cy="6" r="5.2" fill="none" stroke="#a51d1c"/><ellipse cx="6" cy="6" rx="2.3" ry="5.2" fill="none" stroke="#a51d1c"/><line x1="0.8" y1="6" x2="11.2" y2="6" stroke="#a51d1c"/></svg>
        tarvohomes.com.au
      </span>
      <span class="contact">
        <svg viewBox="0 0 12 12"><rect x="0.5" y="2" width="11" height="8" rx="1" fill="none" stroke="#a51d1c"/><polyline points="0.8,2.5 6,6.5 11.2,2.5" fill="none" stroke="#a51d1c"/></svg>
        hello@tarvohomes.com.au
      </span>
    </div>
    <div class="rule"></div>
    <p class="address">14 Kestrel Road, Balcatta Park, Western<br>Australia 6021 PO Box 2208, Balcatta Park WA 6914</p>
  </section>

  <section class="cover-panel">
    <div class="brand-large"><span class="mark"></span>Tarvo Homes</div>
    <svg class="cover-wave" width="405" height="577" viewBox="0 0 405 577">
      <defs>
        <linearGradient id="housePhoto" x1="0" x2="0" y1="0" y2="1">
          <stop offset="0" stop-color="#c0211d"/>
          <stop offset="0.5" stop-color="#a51a17"/>
          <stop offset="1" stop-color="#8c1411"/>
        </linearGradient>
      </defs>
      <path d="M0 303 C69 290 129 307 197 311 C289 316 359 287 405 240 V577 H0 Z" fill="url(#housePhoto)" role="img" aria-label="Red-tinted photo of a new single-storey home frontage"/>
    </svg>
  </section>
</div>
</body>
</html>
```